Redesign criminal justice consulting website

We run a small professional services firm that does research, evaluation, consulting, and training on criminal justice issues. We need to redesign our website (www.brvolquest.com). The existing site is something we made ourselves. It is unprofessional and does not do a good job of communicating what we do or who we are.

We would like the new site to provide a basic overview of what we do. Moreover, we would like it to communicate several themes that represent who we are:

* global

* innovative

* analytical

* practical

We view the principal design challenge as figuring out a subtle, interesting, and graphically appealing way to communicate these themes.

Target Market(s)

Our primary customers are governments, research firms, criminal justice agencies, and schools. The people who we want to find our site are seeking research, evaluation, training, or consulting services related to crime, criminal justice, or policing.

Industry/Entity Type

Consulting

Number of Pages Required

2 pages

Requirements
Must have
• 1. We would like the site to use our logo. It is attached (please use the maroon 4-color version with the company name but without the slogan). The site should also use the colors present in our logo. It may use other colors as well, as long as these colors coordinate with the logo colors.

• 2. For main pages or buttons, we need the following:
• *Home
• *About BVQ
• *Services
• *E-Training
• *Resources
• *Contact BVQ

• 3. We like simple, crisp, subtle designs over "busier," cluttered, or very complex designs.

• 4. We'd like to receive, at a minimum, the home page and a sample inner page.
Nice to have
• We need some help in thinking through what regions or sections should exist on the home page. We are thinking about having a window on there where we can make announcements about recent developments like new reports, new e-training videos, new photographs, etc... We are open to suggestions here.
Should not have
• 1. Gimmicky or overused clipart.
• 2. Cliched images associated with criminal justice, including magnifying glasses, scales of justice, etc... Our logo makes a subtle nod to criminal justice through the use of a fingerprint as the dot on the "J" in the company initials. That''s sufficient for our purposes. Concentrate instead on the themes listed above.
• 3. Major use of colors that don't match our logo, like blue.

```html
<!DOCTYPE html>
<html lang="en">
<head>
<meta charset="utf-8">
<title>BVQ — Home</title>
<link rel="stylesheet" href="https://fonts.googleapis.com/css2?family=Bodoni+Moda:ital,wght@1,400&family=Arimo:wght@400&display=swap">
<style>
  :root {
    --maroon: #7a1f1b;
    --maroon-soft: #b98783;
    --rose: #a3524d;
    --tab-tint: rgba(255, 255, 255, 0.28);
    --quote-grey: #b3b1ae;
    --sidebar-grey: #dedbd8;
    --sidebar-band: #c9aeac;
    --sidebar-edge: #e9e0df;
    --paper: #ffffff;
    --nav-text: #f6eceb;
  }
  * { margin: 0; padding: 0; box-sizing: border-box; }
  html, body {
    width: 1200px; height: 675px; overflow: hidden;
    background: var(--paper);
  }
  .page { position: relative; width: 1200px; height: 675px; }

  .brand {
    position: absolute; left: 0; top: 0; width: 202px; height: 112px;
    display: flex; align-items: center; justify-content: center;
    background: var(--paper);
  }
  .brand-name {
    font-family: "Arimo", sans-serif; font-weight: 400;
    font-size: 40px; color: var(--maroon); letter-spacing: 2px;
  }

  .sidebar {
    position: absolute; left: 0; top: 112px; width: 202px; height: 563px;
    background: linear-gradient(160deg, #e7e4e1 0%, var(--sidebar-grey) 50%, #d2cfcb 100%);
  }
  .sidebar-edge { position: absolute; left: 0; top: 0; width: 20px; height: 100%; background: var(--sidebar-edge); opacity: .8; }
  .sidebar-band { position: absolute; left: 20px; top: 0; width: 66px; height: 100%; background: var(--sidebar-band); opacity: .75; }

  .hero {
    position: absolute; left: 202px; top: 0; width: 927px; height: 85px;
    background: linear-gradient(90deg, #5d5647 0%, #8a826b 22%, #d9d4b6 30%, #ebe7cc 60%, #e2ddc2 100%);
  }

  .nav {
    position: absolute; left: 202px; top: 85px; width: 927px; height: 54px;
    background: linear-gradient(var(--maroon) 0 27px, var(--maroon-soft) 27px 100%);
  }
  .nav ul { list-style: none; display: flex; gap: 3px; }
  .nav li {
    width: 117px; height: 24px; margin-top: 8px;
    background: var(--tab-tint);
    font-family: "Arimo", sans-serif; font-size: 13px; color: var(--nav-text);
    text-transform: uppercase; letter-spacing: .1px;
    padding: 9px 0 0 11px; line-height: 1;
  }

  .mission {
    position: absolute; left: 210px; top: 190px;
    font-family: "Bodoni Moda", serif; font-style: italic; font-weight: 400;
    color: var(--quote-grey); font-size: 27px; letter-spacing: 3px;
  }
  .mission .line { height: 42px; line-height: 42px; white-space: nowrap; }
  .mission em { font-style: italic; color: var(--rose); font-size: 36px; letter-spacing: 3.5px; }
</style>
</head>
<body>
<div class="page">
  <div class="brand">
    <span class="brand-name">BVQ</span>
  </div>

  <div class="sidebar" role="img" aria-label="Faded globe texture in soft grey and rose">
    <div class="sidebar-edge"></div>
    <div class="sidebar-band"></div>
  </div>

  <div class="hero" role="img" aria-label="Sepia photograph of a globe beside a pen resting on printed numbers"></div>

  <nav class="nav">
    <ul>
      <li>Home</li>
      <li>About BVQ</li>
      <li>Services</li>
      <li>E-Training</li>
      <li>Resources</li>
      <li>Contact BVQ</li>
    </ul>
  </nav>

  <blockquote class="mission">
    <div class="line">“Our services are provided by a <em>network of experts</em></div>
    <div class="line">with a <em>variety of backgrounds</em> in social science,</div>
    <div class="line">law enforcement, criminal law, forensics, and other</div>
    <div class="line">professions. Projects range in scope from brief</div>
    <div class="line">consultations, reports, or training sessions to</div>
    <div class="line">comprehensive, multi-year system-wide</div>
    <div class="line">transformation efforts”...</div>
  </blockquote>
</div>
</body>
</html>
```